Bramblecrest IT Solutions Web Design

We are a new business in Perth Australia specializing in supporting Home residential and Small business with their IT requirements
We believe image and presentation is important and having a eye catching, professional, intuitive website is a must.
Although we are still expanding as business the message we would like to convey to users is that they can trust our work.

Services we provide are
Please refer to text file attached

Future services
- Email hosting
- Domain resller
- Cloud services

A wordpress theme i really like is below.
http://www.layoutquarry.example/wordpress-themes/58316.html
Orange colour included is a preference however a colour that goes withg my logo is fine too.

The logo i would like to include is also attached.

I would like the web site design to be built and coded in wordpress and handed over to me so i can continue updating the content, source will be require.

Target Market(s)

Home residential and Small business users

Industry/Entity Type

Residential

Requirements
Must have
• The form to email function in the contact us page.
Nice to have
• Interactive icons

```html
<!DOCTYPE html>
<html lang="en">
<head>
<meta charset="utf-8">
<title>Bramblecrest IT Solutions</title>
<link rel="stylesheet" href="https://fonts.googleapis.com/css2?family=Open+Sans:ital,wght@0,400;0,600;0,700;1,400&display=swap">
<style>
:root{
  --orange:#f7931e;
  --header:#858585;
  --nav:#efefed;
  --band:#8c8c8c;
  --light:#f5f4f2;
  --mid:#ecebe8;
  --ink:#222;
  --text:#555;
  --rule:#c9c9c6;
  --dark:#4a4a4a;
  --panel:#2f2f2f;
  --footer:#232323;
  --bottom:#3c3c3c;
  --btn:#3a3a3a;
}
*{box-sizing:border-box;margin:0;padding:0}
html,body{width:1200px;height:2236px;overflow:hidden}
body{font-family:"Open Sans",Arial,sans-serif;color:var(--text);background:var(--light);position:relative}
.abs{position:absolute}

/* header */
.site-header{position:absolute;left:0;top:0;width:1200px;height:64px;background:var(--header);border-bottom:3px solid var(--orange)}
.brand{position:absolute;left:104px;top:10px;display:flex;align-items:center;gap:10px}
.brand-mark{width:40px;height:40px;background:var(--ink)}
.brand-name{font-weight:700;font-size:26px;color:var(--orange);line-height:1}
.contact-top{position:absolute;top:14px;display:flex;align-items:center;gap:12px;color:#fff;font-weight:700;font-size:15px;white-space:nowrap}
.contact-top .ico{width:36px;height:34px;background:var(--orange);display:flex;align-items:center;justify-content:center;flex:none}
.main-nav{position:absolute;left:0;top:64px;width:1200px;height:37px;background:var(--nav);border-bottom:1px solid #ddd}
.main-nav ul{list-style:none;display:flex;gap:22px;margin-left:106px;line-height:37px;font-size:13px;color:#666}

/* hero */
.hero-photo{position:absolute;left:0;top:101px;width:1200px;height:266px;background:linear-gradient(90deg,#dcdcdc,#efefef 40%,#e6e4e0 70%,#d9d9d9)}
.hero-caption{position:absolute;left:104px;top:240px;width:992px;height:67px;background:rgba(120,120,120,.75);display:flex;align-items:center}
.hero-caption h2{font-size:28px;font-weight:600;color:var(--orange);width:346px;padding-left:52px}
.hero-caption p{color:#fff;font-weight:700;font-size:12px;line-height:19px;width:460px}
.hero-dots{position:absolute;left:104px;top:323px;width:105px;height:22px;background:#8e8e8e;display:flex;gap:8px;padding:6px 8px}
.hero-dots span{width:11px;height:10px;background:#fff}
.hero-dots span:first-child{background:var(--orange);border-radius:50%}

.partners{position:absolute;left:0;top:367px;width:1200px;height:61px;background:var(--band);display:flex;padding-left:88px}
.partner{width:170px;border-right:1px solid #a5a5a5;display:flex;align-items:center;justify-content:center;gap:8px;color:#fff;font-size:20px;font-weight:600}
.partner i{width:14px;height:14px;border-radius:50%;background:#fff;display:block}

/* shared section */
.eyebrow{color:var(--orange);font-weight:600;font-size:19px}
.section-title{color:var(--ink);font-weight:700;font-size:30px;line-height:38px}
.section-lead{font-size:13px;line-height:19px;color:#444;margin-top:6px}
.divider{position:absolute;width:1px;background:var(--rule)}
.notch{position:absolute;width:20px;height:20px;border-left:1px solid var(--rule);border-bottom:1px solid var(--rule)}

/* services */
.services{position:absolute;left:0;top:428px;width:1200px;height:340px;background:var(--light);border-bottom:1px solid #ddd}
.feature-title{position:absolute;font-weight:700;font-size:16px;color:var(--ink)}
.feature-card{position:absolute;width:310px;height:52px;background:#ebebea;border:1px solid #d8d8d6;font-size:13px;line-height:16px;color:#555;display:flex;align-items:center}
.feature-icon{position:absolute;width:54px;height:54px;border-radius:50%;background:var(--orange);border:3px solid #2b2b2b;top:-2px}

/* pricing */
.pricing{position:absolute;left:0;top:768px;width:1200px;height:533px;background:var(--mid);border-bottom:1px solid #ddd}
.tab{position:absolute;top:35px;width:133px;height:44px;background:var(--btn);border-radius:3px;color:#fff;font-weight:600;font-size:18px;display:flex;align-items:center;gap:10px;padding-left:18px}
.tab:after{content:"";position:absolute;left:36px;bottom:-10px;border:10px solid transparent;border-top-color:var(--btn);border-bottom:0}
.tab.active{background:#1e1e1e}
.tab.active:after{border-top-color:#1e1e1e}
.tab i{width:16px;height:16px;background:#fff;border-radius:2px;display:block}
.feature-table{position:absolute;left:104px;top:150px;width:600px;border-collapse:collapse}
.feature-table th{font-size:17px;font-weight:600;color:#333;text-align:center;height:43px;border-bottom:1px solid var(--rule)}
.feature-table th:first-child{text-align:left}
.feature-table td{font-size:14px;height:47px;border-bottom:1px solid #d6d6d3;color:#555;text-align:center}
.feature-table td:first-child{text-align:left}
.mark{display:inline-block;width:22px;height:22px;border-radius:50%;background:#2d2d2d;vertical-align:middle}
.mark svg{display:block}
.trial{position:absolute;left:800px;top:150px;width:296px;text-align:right}
.trial .eyebrow{font-size:19px;color:var(--orange);margin:0}
.trial .lead{font-size:16px;line-height:24px;color:#555;margin-top:18px}
.btn{display:inline-block;background:var(--btn);color:#fff;font-weight:600;font-size:19px;height:42px;line-height:42px;padding:0 16px;margin-left:32px}

/* results */
.results{position:absolute;left:0;top:1301px;width:1200px;height:310px;background:var(--light)}
.stats{position:absolute;left:446px;top:92px;display:flex;align-items:flex-start}
.stat .icon{height:22px;color:#333;font-size:16px;font-weight:600}
.stat .num{color:var(--orange);font-weight:700;font-size:25px;margin-top:6px}
.stat .label{color:#222;font-weight:700;font-size:12px;line-height:18px;margin-top:6px;text-transform:uppercase}
.op{width:38px;font-size:24px;color:#333;font-weight:600;padding-top:30px}

/* widgets */
.widgets{position:absolute;left:0;top:1611px;width:1200px;height:361px;background:var(--dark)}
.widget{position:absolute;top:54px;width:306px}
.widget h3{color:#fff;font-size:25px;font-weight:600;display:flex;align-items:center;gap:16px;height:36px}
.tag-btn{background:#2a2a2a;color:#fff;font-size:12px;font-weight:400;padding:4px 12px}
.widget .box{background:var(--panel);height:200px;margin-top:12px;position:relative;overflow:hidden}
.photo{height:122px;background:linear-gradient(180deg,#6fa9da 0%,#a9cfe8 45%,#5b7d6a 75%,#3e5546 100%)}
.box .caption{color:#eee;font-style:italic;font-size:14px;line-height:20px;padding:8px 10px}
.tweet{padding:14px 10px 6px 56px;position:relative;color:#eee;font-size:12.5px;line-height:19px}
.tweet time{display:block;font-size:10px;font-style:italic;border-bottom:1px solid #777;padding-bottom:3px;margin-bottom:6px}
.tweet svg{position:absolute;left:16px;top:42px}
.post{padding:10px 14px 0 56px;position:relative;color:#eee;font-size:12.5px;line-height:19px}
.post h4{font-weight:400;font-size:15px;border-bottom:1px solid #888;display:flex;justify-content:space-between;align-items:baseline;padding-bottom:2px;margin-bottom:4px}
.post h4 small{font-size:10px;font-style:italic}
.byline{display:block;text-align:right;font-size:10px;font-style:italic;line-height:14px;margin-top:-3px;margin-bottom:2px}
.date{position:absolute;left:12px;width:32px;height:34px;background:var(--orange);color:#fff;font-weight:700;font-size:13px;line-height:15px;text-align:center;padding-top:2px}

/* footer */
.site-footer{position:absolute;left:0;top:1972px;width:1200px;height:219px;background:var(--footer);border-top:2px solid var(--orange)}
.quote{position:absolute;left:104px;top:50px;width:221px;height:102px;background:#4c4c4c;color:#eee;font-style:italic;font-size:12.5px;line-height:19px;padding:10px 12px}
.quote:after{content:"";position:absolute;left:150px;bottom:-12px;border:12px solid transparent;border-top-color:#4c4c4c;border-bottom:0}
.quote-author{position:absolute;left:104px;top:168px;width:221px;text-align:right;font-style:italic;color:#ccc;font-size:11px}
.footer-title{position:absolute;top:48px;color:#fff;font-weight:700;font-size:17px}
.email-field{position:absolute;left:358px;top:86px;width:224px;height:24px;background:#e9e9e9;border:1px solid #bbb;font-size:11px;color:#777;padding:4px 6px}
.register{position:absolute;left:358px;top:126px;background:#4c4c4c;color:#eee;font-size:11px;padding:3px 6px}
.tags{position:absolute;left:619px;top:84px;display:flex;flex-direction:column;gap:8px}
.tags div{display:flex;gap:8px}
.tags span{background:#4c4c4c;color:#ddd;font-size:11.5px;padding:3px 9px}
.tags span.on{background:var(--orange);color:#fff}
.contact-list{position:absolute;left:877px;top:92px;list-style:none;color:#ddd;font-size:11.5px}
.contact-list li{display:flex;align-items:center;gap:9px;height:29px}
.contact-list b{color:#fff;font-weight:600}
.bottom-bar{position:absolute;left:0;top:2191px;width:1200px;height:45px;background:var(--bottom);color:#ddd;font-size:12px}
.bottom-bar p{position:absolute;left:104px;top:14px}
.social{position:absolute;right:106px;top:13px;display:flex;gap:24px}
.social i{display:block;width:18px;height:18px;border-radius:50%;background:#e8e8e8}
</style>
</head>
<body>

<header class="site-header">
  <div class="brand"><span class="brand-mark"></span><span class="brand-name">Bramblecrest IT Solutions</span></div>
  <div class="contact-top" style="left:680px">
    <span class="ico"><svg width="18" height="13" viewBox="0 0 18 13"><rect x=".5" y=".5" width="17" height="12" fill="#fff"/><path d="M1 1l8 6 8-6" stroke="#f7931e" fill="none" stroke-width="1.5"/></svg></span>info@bramblecrest.example
  </div>
  <div class="contact-top" style="left:960px">
    <span class="ico"><svg width="18" height="16" viewBox="0 0 18 16"><path d="M2 5c0-3 14-3 14 0l-3 1-1-2H6L5 6z" fill="#fff"/><rect x="4" y="8" width="10" height="6" rx="1" fill="#fff"/></svg></span>555 010 274
  </div>
</header>

<nav class="main-nav">
  <ul><li>Home</li><li>Abour</li><li>Services</li><li>Work</li><li>Features</li><li>Pricign</li><li>Contact</li></ul>
</nav>

<section class="hero">
  <div class="hero-photo" role="img" aria-label="Hands holding a smartphone with a bright blue screen against a light grey background"></div>
  <div class="hero-caption">
    <h2>Our Grea Team</h2>
    <p>E PARTNER WITH CREATIVE MINDS AND BIG THINKERS TO ENGINEER AND BUILD AWARD-WINNING INTERACTIVE PROJECTS</p>
    <svg class="abs" style="right:74px;top:20px" width="50" height="28" viewBox="0 0 50 28"><path d="M0 14h44M32 2l14 12-14 12" stroke="#e3c500" stroke-width="5" fill="none"/></svg>
  </div>
  <div class="hero-dots"><span></span><span></span><span></span><span></span></div>
</section>

<div class="partners">
  <div class="partner"><i></i>roastly</div>
  <div class="partner"><i></i>Hexfield</div>
  <div class="partner">Crownway</div>
  <div class="partner"><i></i>cubeworks</div>
  <div class="partner"><i></i>pairly</div>
  <div class="partner"><i></i>roastly</div>
  <div class="partner" style="border-right:0">Crownway</div>
</div>

<section class="services">
  <div class="abs" style="left:104px;top:70px;width:300px">
    <p class="eyebrow">What we do</p>
    <h2 class="section-title">simplify your business processes</h2>
    <p class="section-lead">Sollemnes wisi enim ad minim veniam, quis nostrud exerci tation ullamcorper suscipit lobortis nisl ut aliquip consequat.</p>
  </div>
  <div class="divider" style="left:410px;top:72px;height:200px"></div>
  <div class="notch" style="left:400px;top:147px;background:var(--light);transform:rotate(-135deg)"></div>

  <h3 class="feature-title" style="left:598px;top:66px">Responsive&nbsp; Desing</h3>
  <h3 class="feature-title" style="left:789px;top:66px">Retina Desing</h3>
  <h3 class="feature-title" style="left:639px;top:170px">Full Validated</h3>
  <h3 class="feature-title" style="left:789px;top:170px">Social Media</h3>

  <div class="feature-card" style="left:450px;top:98px;padding-left:58px">Pellentesque habitant morbi tristique senectus et netus et malesuada.<span class="feature-icon" style="left:0"></span></div>
  <div class="feature-card" style="left:788px;top:98px;padding-left:10px;text-align:right;padding-right:56px">Pellentesque habitant morbi tristique senectus et netus et malesuada.<span class="feature-icon" style="right:-10px"></span></div>
  <div class="feature-card" style="left:450px;top:202px;padding-left:58px">Pellentesque habitant morbi tristique senectus et netus et malesuada.<span class="feature-icon" style="left:0"></span></div>
  <div class="feature-card" style="left:788px;top:202px;padding-left:10px;text-align:right;padding-right:56px">Pellentesque habitant morbi tristique senectus et netus et malesuada.<span class="feature-icon" style="right:-10px"></span></div>
</section>

<section class="pricing">
  <div class="tab active" style="left:104px"><i></i>Desktop</div>
  <div class="tab" style="left:274px"><i></i>Laptop</div>
  <div class="tab" style="left:445px"><i></i>Server</div>
  <div class="tab" style="left:616px"><i></i>Mobile</div>

  <table class="feature-table">
    <tr><th>Features</th><th>Account free</th><th>Account Premium</th></tr>
    <tr><td>Complete Social Marketing Suite</td><td><span class="mark"><svg width="22" height="22"><path d="M6 11l4 4 6-7" stroke="#fff" stroke-width="2.4" fill="none"/></svg></span></td><td><span class="mark"><svg width="22" height="22"><path d="M6 11l4 4 6-7" stroke="#fff" stroke-width="2.4" fill="none"/></svg></span></td></tr>
    <tr><td>Social Network</td><td><span class="mark"><svg width="22" height="22"><path d="M6 11l4 4 6-7" stroke="#fff" stroke-width="2.4" fill="none"/></svg></span></td><td><span class="mark"><svg width="22" height="22"><path d="M6 11l4 4 6-7" stroke="#fff" stroke-width="2.4" fill="none"/></svg></span></td></tr>
    <tr><td>Full Responsive Web&nbsp; Desing</td><td><span class="mark"><svg width="22" height="22"><path d="M6 11l4 4 6-7" stroke="#fff" stroke-width="2.4" fill="none"/></svg></span></td><td><span class="mark"><svg width="22" height="22"><path d="M6 11l4 4 6-7" stroke="#fff" stroke-width="2.4" fill="none"/></svg></span></td></tr>
    <tr><td>Retina Desing</td><td><span class="mark"><svg width="22" height="22"><path d="M7 7l8 8M15 7l-8 8" stroke="#fff" stroke-width="2.4"/></svg></span></td><td><span class="mark"><svg width="22" height="22"><path d="M6 11l4 4 6-7" stroke="#fff" stroke-width="2.4" fill="none"/></svg></span></td></tr>
    <tr><td>Scripts And Plugins</td><td><span class="mark"><svg width="22" height="22"><path d="M7 7l8 8M15 7l-8 8" stroke="#fff" stroke-width="2.4"/></svg></span></td><td><span class="mark"><svg width="22" height="22"><path d="M6 11l4 4 6-7" stroke="#fff" stroke-width="2.4" fill="none"/></svg></span></td></tr>
    <tr><td>Full Documentation And Support</td><td><span class="mark"><svg width="22" height="22"><path d="M7 7l8 8M15 7l-8 8" stroke="#fff" stroke-width="2.4"/></svg></span></td><td><span class="mark"><svg width="22" height="22"><path d="M6 11l4 4 6-7" stroke="#fff" stroke-width="2.4" fill="none"/></svg></span></td></tr>
  </table>

  <div class="divider" style="left:783px;top:157px;height:270px"></div>
  <div class="notch" style="left:773px;top:240px;background:var(--mid);transform:rotate(45deg)"></div>
  <div class="trial">
    <p class="eyebrow">Get started</p>
    <h2 class="section-title">today witha a free trial!</h2>
    <p class="lead">30 days free trial | No credit card required | $13/mo after end of trial period</p>
    <div style="margin-top:26px"><span class="btn">Try Free</span><span class="btn">Buy now</span></div>
  </div>
</section>

<section class="results">
  <div class="abs" style="left:104px;top:56px;width:300px">
    <p class="eyebrow">Our Results</p>
    <h2 class="section-title">A fact worth a thousand words</h2>
    <p class="section-lead">Sollemnes wisi enim ad minim veniam, quis nostrud exerci tation ullamcorper suscipit lobortis nisl ut aliquip consequat.</p>
  </div>
  <div class="divider" style="left:410px;top:50px;height:218px"></div>
  <div class="notch" style="left:400px;top:124px;background:var(--light);transform:rotate(-135deg)"></div>

  <div class="stats">
    <div class="stat" style="width:143px"><div class="icon"><svg width="70" height="20"><g fill="none" stroke="#333" stroke-width="2"><circle cx="10" cy="11" r="7"/><circle cx="35" cy="11" r="7"/><circle cx="60" cy="11" r="7"/></g></svg></div><div class="num">1,000,123</div><div class="label">Hours worked<br>since 2003</div></div>
    <div class="op">+</div>
    <div class="stat" style="width:150px"><div class="icon">&lt;/html&gt;</div><div class="num">6,233,954</div><div class="label">Lines<br>of codec</div></div>
    <div class="op">+</div>
    <div class="stat" style="width:72px"><div class="icon"><svg width="20" height="18"><rect x="1" y="4" width="18" height="13" fill="#333"/></svg></div><div class="num">780</div><div class="label">Clients<br>served</div></div>
    <div class="op">+</div>
    <div class="stat" style="width:86px"><div class="icon"><svg width="20" height="18"><path d="M2 4l8-3 8 3-8 4z M2 6l8 4 8-4v8l-8 4-8-4z" fill="#333"/></svg></div><div class="num">520</div><div class="label">Projects<br>completed</div></div>
    <div class="op">=</div>
    <div class="stat" style="width:90px"><div class="icon"><svg width="20" height="18"><rect x="1" y="5" width="18" height="12" fill="#333"/><rect x="6" y="1" width="8" height="5" fill="none" stroke="#333" stroke-width="2"/></svg></div><div class="num">18</div><div class="label">Years of<br>experience</div></div>
  </div>
</section>

<section class="widgets">
  <div class="widget" style="left:104px">
    <h3>About</h3>
    <div class="box">
      <div class="photo" role="img" aria-label="Two hikers on a rocky summit overlooking a blue sea and distant islands"></div>
      <p class="caption">A small team of designers and developers, who help brands with big ideas.</p>
    </div>
  </div>
  <div class="widget" style="left:447px">
    <h3>Newsfeed <span class="tag-btn">Follow Us</span></h3>
    <div class="box">
      <div class="tweet"><time>6:34 AM Oct 14</time>UX design for startups: efficient design techniques @lenawright&nbsp; @marketfolk<svg width="24" height="20"><ellipse cx="12" cy="12" rx="11" ry="7" fill="#777"/></svg></div>
      <div class="tweet"><time>6:34 AM Oct 14</time>UX design for startups: efficient design techniques @lenawright&nbsp; @marketfolk<svg width="24" height="20"><ellipse cx="12" cy="12" rx="11" ry="7" fill="#777"/></svg></div>
    </div>
  </div>
  <div class="widget" style="left:790px">
    <h3>Blog <span class="tag-btn">Subscribe</span></h3>
    <div class="box">
      <div class="post"><h4>Title Entry Blog <small>By lenawright</small></h4>UX design for startups: efficient design techniques @lenawright&nbsp; @marketfolk<span class="date" style="top:44px">20<br>Feb</span></div>
      <div class="post"><h4>Title Entry Blog</h4><span class="byline">February 9, 2013 By lenawright</span>UX design for startups: efficient design techniques @lenawright&nbsp; @marketfolk<span class="date" style="top:56px">20<br>Feb</span></div>
    </div>
  </div>
</section>

<footer class="site-footer">
  <blockquote class="quote">Lorem ipsum ea cum congue bono-rum, pri no natum clita. His ne vide omnis forensibus. Eum cetero imper-diet et.!</blockquote>
  <p class="quote-author">Mara Ellison, Web Designer</p>

  <h4 class="footer-title" style="left:359px">Newsletter</h4>
  <div class="email-field">Your Email</div>
  <span class="register">Register</span>

  <h4 class="footer-title" style="left:619px">Tag Cloud</h4>
  <div class="tags">
    <div><span>Blog</span><span>Web Desing</span><span>Blog</span></div>
    <div><span>News</span><span class="on">Internet</span><span>Audio</span><span>Image</span></div>
    <div><span>Blog</span><span>Web Desing</span><span>Blog</span></div>
  </div>

  <h4 class="footer-title" style="left:877px">Contact Us</h4>
  <ul class="contact-list">
    <li><svg width="11" height="8"><rect width="11" height="8" fill="#fff"/></svg><span><b>E-Mail Us:</b>&nbsp; hello@bramblecrest.example</span></li>
    <li><svg width="11" height="11"><path d="M2 1l3 0 1 3-2 1c1 2 2 3 4 4l1-2 3 1v3C5 11 0 6 2 1z" fill="#fff"/></svg><span><b>Call Us at:</b>&nbsp; 55-5010-2741</span></li>
    <li><svg width="10" height="13"><path d="M5 0a5 5 0 0 1 5 5c0 3-5 8-5 8S0 8 0 5a5 5 0 0 1 5-5z" fill="#fff"/><circle cx="5" cy="5" r="2" fill="#232323"/></svg><span><b>Location:</b>&nbsp; Cll 8 # 21 - 40 - Harbourton</span></li>
  </ul>
</footer>

<div class="bottom-bar">
  <p>© 2015 Bramblecrest IT Solutions All rights reserved.</p>
  <div class="social"><i></i><i></i><i></i><i></i></div>
</div>

</body>
</html>
```